The B.O.L.D. Initiative Display Poster

We need a design for a Display Poster (33"W x 73"H) for an expo we are attending May 9th.

Our website is www.boldinitiative-example.org for more information

We are a 501(c)3 that works with youth who have been commercially sexual exploited. We have a California Licensed Therapeutic Residential Program, Drop-In Center and Thrift Store.

B.O.L.D. stands for Brave, Open, Lively and Determined

Our Full logo and Logo without Text is attached. Our mission is:
"Empowers youth to break away from Commercial Sexual Exploitation and Evolve from Victims to Leaders"

We want the design to highlight to phoenix logo, as well as indicate our mission statement.

The B.O.L.D. Initiative offers the following for youth who have been commercially sexually exploited:

• A California licensed (level 12) therapeutic residential program (GROWING at home)
• A drop-in center (open 3pm-7pm Mondays through Fridays) (GROWING forward)
• A Thrift Store where 100% of the proceeds benefit The B.O.L.D. Initiative (GROWING beyond)
The B.O.L.D. Initiative is:
• Survivor-Led
• Trauma Informed
• Strengths Based
• Culturally and Gender Responsive
• A model utilizing Harm Reduction coupled with Empowerment

Target Market(s)

Non-Profits, Possible Grant Organizations, Youth who have been commercially sexually exploited as children (CSEC)

Font styles to use
Serif

Colors
f68e4e
faa54b
fece3e
fbed22
9bcb3c
886aae
b768aa

Requirements
Must have
• Positive, empowering imagery.
Nice to have
• Inspiring imagery. want to inspire hope, strength, resilience
Should not have
• Negative, chains, imprisonment imagery

```html
<!DOCTYPE html>
<html lang="en">
<head>
<meta charset="utf-8">
<title>The B.O.L.D. Initiative – Display Poster</title>
<link rel="stylesheet" href="https://fonts.googleapis.com/css2?family=Source+Sans+3:wght@400;600;700;900&display=swap">
<style>
  :root{
    --purple:#886aae;
    --purple-deep:#4e2a78;
    --orchid:#b768aa;
    --green:#9bcb3c;
    --yellow:#fbed22;
    --gold:#fece3e;
    --amber:#faa54b;
    --orange:#f68e4e;
    --ink:#3a2a55;
    --paper:#ffffff;
  }
  *{margin:0;padding:0;box-sizing:border-box}
  html,body{width:751px;height:1200px;overflow:hidden;background:var(--paper)}
  .poster{position:relative;width:751px;height:1200px;overflow:hidden;background:var(--paper);font-family:"Source Sans 3",sans-serif;color:var(--ink)}
  .ribbons{position:absolute;inset:0;width:100%;height:100%}
  .brand{position:absolute;top:150px;left:70px;display:flex;align-items:center;gap:28px}
  .brand-dot{width:150px;height:150px;border-radius:50%;background:var(--purple-deep)}
  .brand-name{font-weight:600;font-size:46px;line-height:1.05;color:var(--purple-deep)}
  .mission{position:absolute;top:575px;left:0;width:100%;text-align:center;color:var(--ink)}
  .mission-key{font-weight:900;font-size:58px;letter-spacing:1px;color:var(--orange);text-shadow:2px 3px 3px rgba(60,30,80,.45);line-height:1}
  .mission-line{font-size:36px;line-height:1.3;color:#3b2c4f}
  .mission-key + .mission-line{margin-top:8px}
  .mission-gap{height:30px}
  .services{position:absolute;top:905px;left:0;width:100%;text-align:center;font-size:13px;line-height:1.3;color:#3b2c4f}
  .services h2{font-size:13px;font-weight:700;margin-bottom:2px}
  .services ul{list-style:none;margin-bottom:10px}
  .services ul:last-child{margin-bottom:0}
  .services li::before{content:"• "}
  .contact{position:absolute;top:1150px;left:0;width:100%;text-align:center;font-size:17px;font-weight:700;color:var(--purple-deep)}
</style>
</head>
<body>
<main class="poster">
  <svg class="ribbons" viewBox="0 0 751 1200" preserveAspectRatio="none" aria-hidden="true">
    <defs>
      <linearGradient id="g-purple" x1="0" y1="0" x2="1" y2="1">
        <stop offset="0" stop-color="#9a74bd"/><stop offset="1" stop-color="#7a58a6"/>
      </linearGradient>
      <linearGradient id="g-green" x1="0" y1="0" x2="0" y2="1">
        <stop offset="0" stop-color="#fbed22"/><stop offset=".45" stop-color="#b8d832"/><stop offset="1" stop-color="#9bcb3c"/>
      </linearGradient>
      <linearGradient id="g-orange" x1="0" y1="0" x2="0" y2="1">
        <stop offset="0" stop-color="#f68e4e"/><stop offset=".6" stop-color="#faa54b"/><stop offset="1" stop-color="#fece3e"/>
      </linearGradient>
    </defs>
    <path d="M0 0 H180 C120 220 260 420 520 640 C640 740 720 860 751 960 V1200 H640 C560 980 380 860 200 700 C60 570 0 420 0 260 Z" fill="url(#g-purple)"/>
    <path d="M470 0 H751 V40 C600 160 520 380 420 600 C330 800 220 960 160 1200 H0 V820 C140 720 300 560 380 360 C420 240 440 100 470 0 Z" fill="url(#g-green)" opacity=".95"/>
    <path d="M751 380 V1200 H560 C560 1040 600 860 660 700 C700 590 730 480 751 380 Z" fill="url(#g-orange)"/>
    <path d="M751 700 V1200 H700 C690 1060 710 880 751 700 Z" fill="var(--purple)"/>
    <path d="M0 0 H560 C420 60 300 220 260 420 C220 300 150 160 0 120 Z" fill="#fff" opacity=".85"/>
    <path d="M120 520 C300 640 560 650 751 560 V740 C560 800 300 760 120 680 Z" fill="#fff" opacity=".18"/>
  </svg>

  <header class="brand">
    <div class="brand-dot"></div>
    <div class="brand-name">The B.O.L.D.<br>Initiative</div>
  </header>

  <section class="mission">
    <p class="mission-key">EMPOWERS</p>
    <p class="mission-line">youth to break away from</p>
    <p class="mission-line">Commercial Sexual Exploitation</p>
    <div class="mission-gap"></div>
    <p class="mission-key">EVOLVE</p>
    <p class="mission-line">from Victims to Leaders</p>
  </section>

  <section class="services">
    <h2>The B.O.L.D. Initiative offers the following<br>for youth who have been commercially sexually exploited:</h2>
    <ul>
      <li>A California licensed (level 12) therapeutic residential program (GROWING at home)</li>
      <li>A drop-in center (open 3pm-7pm Mondays through Fridays) (GROWING forward)</li>
      <li>A Thrift Store where 100% of the proceeds benefit The B.O.L.D. Initiative (GROWING beyond)</li>
    </ul>
    <h2>The B.O.L.D. Initiative is:</h2>
    <ul>
      <li>Survivor-Led</li>
      <li>Trauma Informed</li>
      <li>Strengths Based</li>
      <li>Culturally and Gender Responsive</li>
      <li>A model utilizing Harm Reduction coupled with Empowerment</li>
    </ul>
  </section>

  <p class="contact">The B.O.L.D. Initiative hello@boldinitiative-example.org &nbsp;or&nbsp; Call us 555.201.4870</p>
</main>
</body>
</html>
```